Financial Advisor Resource Firm needs business card design

Need business card design for company in Omaha NE called Tallowbrook Partners. We provide resources to financial advisors....workshop programs, retirement analysis, and insurance planning. I would like to see designs that use grays, greens, black, and white colors. The final design should communicate 'collaboration' and be simple yet attractive to financial planning clients. I will attached our logo and another picture of a puzzle piece coming together. I would like the incorporate the puzzle picture somehow, maybe on the back somehow, with color or just the gray scale....OR, the picture be the front of the card with 'Tallowbrook' definition on it (see upload) and then company logo, employee name, title, address on the back (see ppt uploaded). The following disclosure needs to be included somewhere- Advisory services offered through Marlowe Ridge Advisors, LLC.
Updates

I uploaded a svg and ai file of the logo

Target Market(s)

Financial planning clients and financial advisors....so pretty diverse age range of about 40-70.

Industry/Entity Type

Financial Planning

Contact Information for Business Card

Dennis K. Holloway, MBA
Founder/President
5727 E. Larkspur Avenue
Suite 418
Omaha, NE 68297
Phone- (402) 555-0147
Cell- (402) 555-0183
Fax- (402) 555-0129
email- dennis@tallowbrookgroup.example
web address- www.tallowbrookgroup.example

Colors
1b1b1b
474747
d3d3d3
ffffff
9bcb3c
abd036

Requirements
Must have
• Must include logo provided, must be 2 sided, and must have disclosure...all of these items listed in project description

```html
<!DOCTYPE html>
<html lang="en">
<head>
<meta charset="utf-8">
<title>Tallowbrook Partners – Business Card</title>
<link rel="stylesheet" href="https://fonts.googleapis.com/css2?family=Tinos:wght@400;700&family=Open+Sans:wght@400&display=swap">
<style>
  :root {
    --ink: #1b1b1b;
    --charcoal: #474747;
    --stage: #3b3b3b;
    --silver: #d3d3d3;
    --paper: #ececec;
    --white: #ffffff;
    --green: #9bcb3c;
    --green-deep: #8cbf2e;
  }
  * { margin: 0; padding: 0; box-sizing: border-box; }
  html, body { width: 1200px; height: 1200px; overflow: hidden; }
  body { background: var(--stage); position: relative; font-family: "Tinos", "Times New Roman", serif; }

  .card {
    position: absolute;
    left: 246px;
    width: 708px;
    height: 405px;
    border-radius: 22px;
  }
  .card--front { top: 150px; background: var(--charcoal); border: 2px solid var(--silver); }
  .card--back { top: 625px; background: var(--paper); }

  .wordmark {
    position: absolute;
    left: 0; right: 0;
    display: flex;
    align-items: center;
    justify-content: center;
    gap: 16px;
    font-family: "Tinos", "Times New Roman", serif;
    font-weight: 700;
    letter-spacing: 1px;
  }
  .wordmark__dot { width: 30px; height: 30px; border-radius: 50%; background: var(--green); flex: none; }
  .card--front .wordmark { top: 148px; font-size: 50px; color: var(--silver); }
  .card--back .wordmark { top: 70px; font-size: 42px; color: var(--ink); }

  .web {
    position: absolute;
    top: 296px; left: 0; right: 0;
    text-align: center;
    font-family: "Open Sans", Arial, sans-serif;
    font-size: 25px;
    color: var(--white);
  }

  .disclosure {
    position: absolute;
    top: 136px; left: 0; right: 0;
    text-align: center;
    font-size: 11px;
    color: #d6d6d6;
  }

  .person { position: absolute; left: 346px; top: 183px; }
  .person__name { font-size: 24px; color: var(--ink); line-height: 1; }
  .person__title { font-size: 17px; font-weight: 700; color: var(--green-deep); margin-top: 6px; }
  .rule { position: absolute; left: 52px; top: 226px; width: 284px; height: 3px; background: var(--ink); }

  .contacts { position: absolute; left: 42px; top: 264px; list-style: none; }
  .contacts li { display: flex; align-items: center; gap: 12px; height: 26.5px; font-size: 19px; color: var(--ink); }
  .contacts svg { width: 16px; height: 16px; flex: none; fill: var(--green); }

  .address { position: absolute; left: 471px; top: 304px; font-size: 18.5px; line-height: 1.08; color: var(--ink); font-style: normal; }
</style>
</head>
<body>

<section class="card card--front" aria-label="Card front">
  <div class="wordmark"><span class="wordmark__dot"></span>Tallowbrook Partners</div>
  <p class="web">www.tallowbrookgroup.example</p>
</section>

<section class="card card--back" aria-label="Card back">
  <div class="wordmark"><span class="wordmark__dot"></span>Tallowbrook Partners</div>
  <p class="disclosure">Advisory services offered through Marlowe Ridge Advisors, LLC.</p>

  <div class="person">
    <p class="person__name">Dennis K. Holloway, MBA</p>
    <p class="person__title">Founder/President</p>
  </div>
  <div class="rule"></div>

  <ul class="contacts">
    <li><svg viewBox="0 0 16 16"><path d="M4 1h8v14H4z M5.5 2.5v9h5v-9z"/></svg>(402) 555-0183</li>
    <li><svg viewBox="0 0 16 16"><path d="M4 1h8v4H4z M1 6h14v6h-3v3H4v-3H1z M5.5 10v3.5h5V10z"/></svg>(402) 555-0129</li>
    <li><svg viewBox="0 0 16 16"><path d="M3 1.5l3 0 1 3.5-2 1.2a8 8 0 0 0 4.8 4.8L11 9l3.5 1v3c0 .8-.7 1.5-1.5 1.5A12.5 12.5 0 0 1 1.5 3c0-.8.7-1.5 1.5-1.5z"/></svg>(402) 555-0147</li>
    <li><svg viewBox="0 0 16 16"><path d="M1 3h14v10H1z M2 4l6 5 6-5z" fill-rule="evenodd"/></svg>dennis@tallowbrookgroup.example</li>
  </ul>

  <address class="address">5727 E. Larkspur Avenue<br>Suite 418<br>Omaha, NE 68297</address>
</section>

</body>
</html>
```